Startup Drone Platform Company business card

We are needing a business card design for our employees. We are a startup drone platform. We are looking for a business card that has our logo on one side, with the employee/company details on the opposite side. We are looking for something that is very eye catching, modern, and bold.

Target Market(s)

This will target both drone pilots and drone businesses, along with all the industries that could utilize drone services (aerial video, aerial photos, inspections, 3d mapping, etc).

Industry/Entity Type

Business

```html
<!DOCTYPE html>
<html lang="en">
<head>
<meta charset="utf-8">
<title>Skylane Works – Business Card</title>
<link href="https://fonts.googleapis.com/css2?family=Montserrat:wght@400;500&family=Roboto+Condensed:wght@400;500&display=swap" rel="stylesheet">
<style>
  :root {
    --backdrop: #d9d8da;
    --card-white: #fbfbfb;
    --card-dark: #2c2c2c;
    --accent: #6bbcc6;
    --ink: #1e1e1e;
    --paper-text: #f2f2f2;
  }
  * { box-sizing: border-box; margin: 0; padding: 0; }
  html, body {
    width: 1200px; height: 990px; overflow: hidden;
    background: var(--backdrop);
  }
  .sheet {
    position: relative; width: 1200px; height: 990px;
    display: flex; align-items: center; justify-content: center; gap: 48px;
  }
  .card {
    position: relative; width: 520px; height: 287px;
    border-radius: 16px; overflow: hidden;
    box-shadow: 0 3px 6px rgba(0,0,0,0.18);
  }
  .card--front { background: var(--card-white); }
  .card--back { background: var(--card-dark); }

  .card__wave { position: absolute; inset: 0; width: 100%; height: 100%; }

  .wordmark {
    position: absolute; left: 0; right: 0;
    display: flex; align-items: center; justify-content: center; gap: 22px;
    font-family: "Montserrat", sans-serif; font-weight: 500;
    font-size: 20px; letter-spacing: 9px;
  }
  .wordmark__dot {
    width: 14px; height: 14px; border-radius: 50%;
    background: var(--accent); flex: none;
  }
  .card--front .wordmark { top: 68px; color: var(--ink); }
  .card--back .wordmark { top: 125px; color: var(--paper-text); }

  .contact {
    position: absolute; left: 0; right: 0; top: 198px;
    display: flex; align-items: center; justify-content: center; gap: 18px;
    font-family: "Roboto Condensed", sans-serif; color: var(--paper-text);
  }
  .contact__person { text-align: right; }
  .contact__name {
    color: var(--accent); font-weight: 500; font-size: 18px; line-height: 24px;
  }
  .contact__role { font-size: 15px; line-height: 22px; }
  .contact__divider { width: 2px; height: 42px; background: var(--accent); }
  .contact__details { font-size: 11.5px; line-height: 15.5px; }
  .contact__label { color: var(--accent); }

  .website {
    position: absolute; left: 0; right: 0; top: 216px; text-align: center;
    font-family: "Montserrat", sans-serif; font-size: 11.5px; color: var(--paper-text);
  }
</style>
</head>
<body>
<main class="sheet">
  <section class="card card--front">
    <svg class="card__wave" viewBox="0 0 520 287" preserveAspectRatio="none" aria-hidden="true">
      <path d="M30,148 Q280,120 520,162 L520,180 Q300,136 30,148 Z" fill="var(--accent)"/>
      <path d="M0,164 Q260,132 520,190 L520,287 L0,287 Z" fill="var(--card-dark)"/>
    </svg>
    <div class="wordmark">
      <span>SKYLANE</span><span class="wordmark__dot"></span><span>WORKS</span>
    </div>
    <div class="contact">
      <div class="contact__person">
        <p class="contact__name">JORDAN ELLERY</p>
        <p class="contact__role">Office Manager</p>
      </div>
      <div class="contact__divider"></div>
      <div class="contact__details">
        <p>1180 Harbor Rd, Fairview, Ohio 45012</p>
        <p><span class="contact__label">T:</span> 555.014.2280 · <span class="contact__label">E:</span> hello@skylaneworks.com</p>
        <p>www.skylaneworks.com</p>
      </div>
    </div>
  </section>

  <section class="card card--back">
    <div class="wordmark">
      <span>SKYLANE</span><span class="wordmark__dot"></span><span>WORKS</span>
    </div>
    <p class="website">www.skylaneworks.com</p>
  </section>
</main>
</body>
</html>
```